Website for "Bright Meadow Ltd" cleaning bsuiness

We require a website to expose our business to the local market. We want to provide background on who we are and what we do but in an easily digestible way. We clean domestic and commercial premises and want to provide a list of all of our services to potential customers. We operate out of Warrington in the UK.

We would like the website to be animated in some way so that the experience of using it is not dull or mundane. This website needs to be an extension of our company.

Target Market(s)

30 - 60 year olds for Domestic plus commercial clients

Industry/Entity Type

Cleaning Service

Coding

Coded - Design and coding required

Number of Pages Required

4 page

Font styles to use
Sans Serif

Colors
0455a3
3176b5
85acd3
cfdeed
ffffff
000000
1b1b1b
c8c8c8
757575

Requirements
Must have
• Logo which has been provided. Theme based around the logo and its colours. Simple layout to avoid confusion.
Nice to have
• Animations where possible to impress the customer.
Should not have
• any pictures of cleaning equipment, fairies, maids etc

```html
<!DOCTYPE html>
<html lang="en">
<head>
<meta charset="utf-8">
<title>Bright Meadow Ltd – Professional Cleaning Services</title>
<link href="https://fonts.googleapis.com/css2?family=Abel&family=Raleway:wght@400;500;600;700;800&display=swap" rel="stylesheet">
<style>
:root{
  --blue:#0455a3;
  --blue-mid:#3176b5;
  --blue-light:#85acd3;
  --blue-pale:#cfdeed;
  --white:#ffffff;
  --black:#000000;
  --ink:#1b1b1b;
  --line:#c8c8c8;
  --grey:#757575;
  --dark-panel:#1d2633;
  --why-blue:#3a7cc4;
  --works-blue:#2f7cc9;
  --email-grey:#7d7d7d;
}
*{margin:0;padding:0;box-sizing:border-box}
html,body{width:1200px;height:4296px;overflow:hidden}
body{font-family:"Raleway",sans-serif;color:var(--ink);background:var(--white);position:relative}
.abs{position:absolute}
.display{font-family:"Abel",sans-serif;font-weight:400}
svg{display:block}

/* Header + hero */
.hero{position:absolute;left:0;top:0;width:1200px;height:624px;overflow:hidden}
.hero-bg{position:absolute;inset:0;background:linear-gradient(100deg,#5a6673 0%,#3e4b59 35%,#4d5a68 60%,#2c3946 100%)}
.hero-shade{position:absolute;inset:0;background:linear-gradient(180deg,rgba(20,30,45,.35),rgba(20,30,45,.55))}
.brand-box{position:absolute;left:178px;top:0;width:154px;height:160px;background:var(--white);display:flex;flex-direction:column;align-items:center;justify-content:center;gap:10px;padding:10px}
.brand-box .dot{width:28px;height:28px;border-radius:50%;background:var(--blue)}
.brand-name{font-family:"Raleway",sans-serif;font-weight:700;color:var(--blue);font-size:19px;line-height:1.15;text-align:center}
.topline{position:absolute;top:16px;left:470px;display:flex;align-items:center;gap:8px;color:var(--white);font-size:14px}
.topline.phone{left:700px}
.socials{position:absolute;top:16px;left:836px;display:flex;gap:14px}
.socials span{width:18px;height:18px;background:var(--white);opacity:.9;border-radius:2px}
.nav{position:absolute;top:76px;left:392px;display:flex;gap:26px;color:var(--white);font-size:13px;font-weight:600;letter-spacing:.3px}
.search{position:absolute;left:977px;top:52px;width:68px;height:63px;background:var(--blue);display:flex;align-items:center;justify-content:center}
.hero-title{position:absolute;top:226px;width:1200px;text-align:center;color:var(--white);font-size:82px;letter-spacing:3px}
.hero-sub{position:absolute;top:344px;width:1200px;text-align:center;color:var(--white);font-family:"Raleway",sans-serif;font-size:38px;font-weight:400}
.btn-blue{position:absolute;background:var(--blue);color:var(--white);display:flex;align-items:center;justify-content:center;font-weight:600;letter-spacing:1px}
.hero-btn{left:481px;top:424px;width:235px;height:57px;font-size:20px;font-family:"Abel",sans-serif;border-radius:3px}
.slides{position:absolute;top:556px;left:533px;display:flex;gap:14px}
.slides span{width:36px;height:5px;background:rgba(255,255,255,.45)}
.slides span.on{background:var(--blue-light)}

/* About */
.about{position:absolute;top:624px;left:0;width:1200px;height:593px}
.about-dark{position:absolute;left:0;top:0;width:598px;height:593px;background:var(--dark-panel);color:var(--white)}
.about-lead{position:absolute;left:40px;top:50px;width:520px;font-size:17.5px;font-weight:700;line-height:1.6}
.about-text{position:absolute;left:40px;width:510px;font-size:12.5px;line-height:1.6;color:#d6dbe1}
.pill{position:absolute;height:38px;border-radius:19px;color:var(--white);font-size:13px;font-weight:700;display:flex;align-items:center;justify-content:center}
.pill.read{left:34px;top:358px;width:115px;background:var(--blue)}
.pill.quote{left:158px;top:358px;width:152px;background:#3b4350;border:1px solid #6b7380}
.stat-num{position:absolute;top:414px;font-family:"Abel",sans-serif;font-size:84px;color:var(--blue-mid);line-height:1}
.stat-label{position:absolute;top:530px;font-size:13px;color:#c0c6ce}
.primary{position:absolute;left:598px;top:0;width:302px;height:593px;background:var(--white)}
.primary h2{position:absolute;left:44px;top:50px;font-size:27px;color:var(--blue);letter-spacing:.5px}
.primary .rule{position:absolute;left:44px;top:90px;width:224px;height:2px;background:var(--blue)}
.svc-title{position:absolute;left:62px;font-size:13px;font-weight:700;color:var(--ink);letter-spacing:.3px}
.svc-text{position:absolute;left:40px;width:230px;font-size:11.5px;line-height:1.6;color:var(--grey)}
.more{position:absolute;left:216px;font-size:11.5px;color:var(--blue);font-weight:600}
.divider{position:absolute;left:40px;width:230px;height:1px;background:var(--line)}
.family-photo{position:absolute;left:900px;top:0;width:300px;height:593px;background:linear-gradient(160deg,#dfe5ec 0%,#b9c6d4 45%,#e9edf1 100%)}

/* How we work / Why choose */
.work{position:absolute;top:1217px;left:0;width:1200px;height:510px}
.work-photo{position:absolute;left:0;top:0;width:598px;height:510px;background:linear-gradient(120deg,#7a7f83 0%,#4b5558 40%,#2f4648 70%,#5f6b70 100%)}
.work-title{position:absolute;left:0;top:150px;width:598px;text-align:center;color:var(--white);font-size:52px;letter-spacing:1px}
.play{position:absolute;left:258px;top:218px}
.why{position:absolute;left:598px;top:0;width:602px;height:510px;background:var(--why-blue);color:var(--white)}
.why h2{position:absolute;top:56px;width:602px;text-align:center;font-size:44px;letter-spacing:1px}
.why .rule{position:absolute;left:158px;top:112px;width:286px;height:2px;background:var(--white)}
.why-item{position:absolute;left:92px}
.why-item .ico{position:absolute;left:0;top:0;width:70px;height:70px;border-radius:50%;border:2px solid var(--white);display:flex;align-items:center;justify-content:center}
.why-item h3{position:absolute;left:86px;top:8px;font-size:21px;font-weight:700;white-space:nowrap}
.why-item p{position:absolute;left:86px;top:42px;font-size:11.5px;white-space:nowrap;color:#e3ecf6}

/* Services */
.services{position:absolute;top:1727px;left:0;width:1200px;height:702px;background:linear-gradient(90deg,#a9adb2 0%,#d7d9db 25%,#e6e7e8 50%,#cfd2d5 75%,#9fa5ab 100%)}
.services h2{position:absolute;top:44px;width:1200px;text-align:center;font-size:56px;color:var(--black);letter-spacing:1px}
.tabs{position:absolute;top:178px;left:430px;display:flex;height:48px}
.tab{display:flex;align-items:center;justify-content:center;font-family:"Abel",sans-serif;font-size:22px;letter-spacing:1px}
.tab.on{width:154px;background:var(--blue);color:var(--white)}
.tab.off{width:195px;background:var(--white);color:var(--ink);border:2px solid var(--blue)}
.card{position:absolute;top:269px;width:278px;height:195px;background:var(--white);box-shadow:0 2px 6px rgba(0,0,0,.15)}
.card .num{position:absolute;left:12px;top:4px;font-family:"Abel",sans-serif;font-size:54px;color:var(--blue-pale)}
.card h3{position:absolute;left:12px;top:82px;font-size:14px;font-weight:800;color:var(--black)}
.card p{position:absolute;left:12px;top:108px;width:254px;font-size:11px;line-height:1.55;color:var(--grey)}
.card .more{left:214px;top:170px}
.arrow{position:absolute;top:381px;width:48px;height:43px;background:#7d8186;display:flex;align-items:center;justify-content:center}
.case-btn{position:absolute;left:467px;top:596px;width:249px;height:57px;background:var(--ink);color:var(--white);font-size:16px;font-weight:800;letter-spacing:.5px;display:flex;align-items:center;justify-content:center}

/* Works */
.works{position:absolute;top:2429px;left:0;width:1200px;height:235px;background:var(--white)}
.works h2{position:absolute;top:40px;width:1200px;text-align:center;font-size:56px;color:var(--black);letter-spacing:1px}
.more-pill{position:absolute;left:1057px;top:57px;width:126px;height:51px;border-radius:26px;background:var(--blue-mid);color:var(--white);font-family:"Abel",sans-serif;font-size:24px;display:flex;align-items:center;justify-content:center}
.works p{position:absolute;top:170px;width:1200px;text-align:center;font-size:15px;color:var(--grey)}
.grid{position:absolute;top:2664px;left:0;width:1200px;height:578px}
.tile{position:absolute;width:400px;height:289px}
.tile.project{background:var(--works-blue);color:var(--white)}
.project h3{position:absolute;left:76px;top:56px;font-family:"Abel",sans-serif;font-size:22px;font-weight:400;letter-spacing:.5px}
.project .line{position:absolute;left:76px;top:92px;width:270px;height:1px;background:rgba(255,255,255,.6)}
.project .row{position:absolute;left:76px;display:flex;align-items:center;gap:12px;font-size:13px}
.project .testi{position:absolute;left:158px;top:207px;width:88px;height:28px;background:var(--white);color:var(--ink);font-size:11px;font-weight:600;display:flex;align-items:center;justify-content:center}

/* Contact */
.contact{position:absolute;top:3242px;left:0;width:1200px;height:610px}
.form{position:absolute;left:0;top:0;width:598px;height:610px;background:linear-gradient(90deg,#ffffff 0%,#f4f5f6 55%,#e3e6ea 100%)}
.form h2{position:absolute;left:34px;top:72px;font-size:20px;font-weight:500;color:var(--ink)}
.form .rule{position:absolute;left:34px;top:108px;width:440px;height:2px;background:var(--ink)}
.lbl{position:absolute;font-size:14px;font-weight:700;color:var(--blue)}
.field{position:absolute;height:1px;background:var(--ink)}
.select{position:absolute;left:306px;top:290px;width:225px;height:28px;border-bottom:1px solid var(--ink);font-size:11px;color:var(--grey);display:flex;align-items:center;justify-content:space-between;padding:0 6px}
.send{position:absolute;left:34px;top:544px;width:115px;height:40px;border-radius:20px;background:var(--blue-mid);color:var(--white);font-size:14px;font-weight:800;display:flex;align-items:center;justify-content:center}
.map{position:absolute;left:598px;top:0;width:302px;height:610px;background:linear-gradient(150deg,#dfe6ed 0%,#cdd8e3 50%,#e4e9ee 100%)}
.info{position:absolute;left:900px;width:300px;color:var(--white);text-align:center;display:flex;flex-direction:column;align-items:center}
.info h3{font-size:19px;font-weight:800;margin-top:14px}
.info p{font-size:13px;margin-top:12px;line-height:1.5}

/* Footer */
.footer{position:absolute;top:3852px;left:0;width:1200px;height:344px;background:var(--white)}
.foot-brand{position:absolute;left:34px;top:56px;display:flex;align-items:center;gap:10px}
.foot-brand .dot{width:20px;height:20px;border-radius:50%;background:var(--blue)}
.foot-brand span{font-weight:700;color:var(--blue);font-size:17px}
.foot-text{position:absolute;left:34px;top:164px;width:520px;font-size:11.5px;line-height:1.65;color:var(--grey)}
.foot-col{position:absolute;top:62px}
.foot-col h4{font-size:15px;font-weight:700;color:var(--ink)}
.foot-col .rule{width:270px;height:1px;background:var(--ink);margin:18px 0 22px}
.foot-col li{list-style:none;font-size:12.5px;color:var(--ink);height:46px}
.to-top{position:absolute;left:1162px;top:310px;width:26px;height:26px;border-radius:50%;border:1px solid var(--blue-light);display:flex;align-items:center;justify-content:center}
.bottom{position:absolute;top:4196px;left:0;width:1200px;height:100px;background:#f0f0f0;border-top:1px solid var(--line)}
.bottom p{position:absolute;left:34px;top:40px;font-size:11.5px;color:var(--grey)}
.bottom .sq{position:absolute;top:36px;display:flex;gap:6px;left:1002px}
.bottom .sq span{width:28px;height:28px;background:#8c8c8c}
</style>
</head>
<body>

<header class="hero">
  <div class="hero-bg" role="img" aria-label="Photo of a bright, tidy dining room and kitchen"></div>
  <div class="hero-shade"></div>

  <div class="brand-box">
    <span class="dot"></span>
    <span class="brand-name">Bright Meadow Ltd</span>
  </div>

  <div class="topline">
    <svg width="16" height="12" viewBox="0 0 16 12"><rect x="0.5" y="0.5" width="15" height="11" fill="none" stroke="#fff"/><path d="M1 1l7 6 7-6" fill="none" stroke="#fff"/></svg>
    info@brightmeadow.co.uk
  </div>
  <div class="topline phone">
    <svg width="14" height="14" viewBox="0 0 24 24"><path d="M6.6 10.8a15 15 0 006.6 6.6l2.2-2.2a1 1 0 011-.25 11.4 11.4 0 003.6.6 1 1 0 011 1V20a1 1 0 01-1 1A17 17 0 013 4a1 1 0 011-1h3.5a1 1 0 011 1 11.4 11.4 0 00.6 3.6 1 1 0 01-.25 1z" fill="#fff"/></svg>
    100-22-480000
  </div>
  <div class="socials"><span></span><span></span><span></span><span></span><span></span></div>

  <nav class="nav">
    <span>HOME</span><span>WHAT WE DO</span><span>DOMESTIC CLEANING</span><span>COMMERCIAL CLEANING</span><span>CONTACT US</span>
  </nav>
  <div class="search">
    <svg width="26" height="26" viewBox="0 0 24 24"><circle cx="10" cy="10" r="7" fill="none" stroke="#fff" stroke-width="2"/><path d="M15 15l6 6" stroke="#fff" stroke-width="2"/></svg>
  </div>

  <h1 class="hero-title display">HIGH QUALITY</h1>
  <p class="hero-sub">Cleaning Service with Affordable Price</p>
  <div class="btn-blue hero-btn">LEARN MORE</div>
  <div class="slides"><span class="on"></span><span></span><span></span></div>
</header>

<section class="about">
  <div class="about-dark">
    <p class="about-lead">Bright Meadow Ltd are leaders in the commercial cleaning sector. Our experience and expertise allows us to achieve and maintain the highest &nbsp;standards of cleanliness.</p>
    <p class="about-text" style="top:200px">We deliver a range of cleaning services to hundreds of clients from daily office cleaning, specialist industrial cleaning, window cleaning, carpet and floor cleaning as well as &nbsp;washroom and hygiene services.</p>
    <p class="about-text" style="top:294px">We are dedicated to delivering an exceptional service, providing the best people, and offering great value for money.</p>
    <div class="pill read">READ MORE</div>
    <div class="pill quote">GET A QUOTE</div>
    <div class="stat-num" style="left:30px">500</div>
    <div class="stat-label" style="left:34px">Happy Clients</div>
    <div class="stat-num" style="left:290px">200</div>
    <div class="stat-label" style="left:292px">Working Hours / Month</div>
  </div>

  <div class="primary">
    <h2 class="display">OUR PRIMARY SERVICE</h2>
    <div class="rule"></div>
    <h3 class="svc-title" style="top:142px">DOMESTIC CLEANING</h3>
    <p class="svc-text" style="top:172px">Regular home visits that keep kitchens, bathrooms and living rooms fresh, with trusted cleaners who follow your own checklist every single week.</p>
    <span class="more" style="top:290px">More &rarr;</span>
    <div class="divider" style="top:322px"></div>
    <h3 class="svc-title" style="top:362px">COMMERCIAL CLEANING</h3>
    <p class="svc-text" style="top:392px">Offices, shops and clinics cleaned before or after hours, using safe products and careful staff so your working day starts bright.</p>
    <span class="more" style="top:510px">More &rarr;</span>
  </div>

  <div class="family-photo" role="img" aria-label="Photo of a smiling family at home"></div>
</section>

<section class="work">
  <div class="work-photo" role="img" aria-label="Photo of a woman relaxing with a laptop in a clean living room"></div>
  <h2 class="work-title display">HOW WE WORK</h2>
  <svg class="play" width="82" height="82" viewBox="0 0 82 82"><circle cx="41" cy="41" r="38" fill="none" stroke="#fff" stroke-width="3"/><path d="M33 26l22 15-22 15z" fill="#fff"/></svg>

  <div class="why">
    <h2 class="display">WHY CHOOSE US</h2>
    <div class="rule"></div>

    <div class="why-item" style="top:160px">
      <div class="ico"><svg width="34" height="34" viewBox="0 0 24 24"><path d="M3 11l9-7 9 7M6 9v11h12V9" fill="none" stroke="#fff" stroke-width="1.8"/></svg></div>
      <h3>Holistic Housekeeping</h3>
      <p>Every room cared for with the same attention to detail.</p>
    </div>
    <div class="why-item" style="top:268px">
      <div class="ico"><svg width="30" height="34" viewBox="0 0 20 24"><rect x="2" y="10" width="16" height="12" rx="2" fill="none" stroke="#fff" stroke-width="1.8"/><path d="M6 10V6a4 4 0 018 0v4" fill="none" stroke="#fff" stroke-width="1.8"/><circle cx="10" cy="16" r="1.8" fill="#fff"/></svg></div>
      <h3>STRICT SECURITY</h3>
      <p>Vetted staff, secure keys and full insurance as standard.</p>
    </div>
    <div class="why-item" style="top:370px">
      <div class="ico"><svg width="38" height="30" viewBox="0 0 30 22"><circle cx="15" cy="6" r="4" fill="none" stroke="#fff" stroke-width="1.6"/><path d="M8 20a7 7 0 0114 0" fill="none" stroke="#fff" stroke-width="1.6"/><circle cx="5" cy="9" r="3" fill="none" stroke="#fff" stroke-width="1.4"/><circle cx="25" cy="9" r="3" fill="none" stroke="#fff" stroke-width="1.4"/><path d="M0 20a5 5 0 018-4M30 20a5 5 0 00-8-4" fill="none" stroke="#fff" stroke-width="1.4"/></svg></div>
      <h3>TRUSTED TEAM</h3>
      <p>Local cleaners who know your home and your routine.</p>
    </div>
  </div>
</section>

<section class="services" role="region" aria-label="Our services">
  <h2 class="display">OUR SERVICES</h2>
  <div class="tabs"><div class="tab on">DOMESTIC</div><div class="tab off">COMMERCIAL</div></div>

  <div class="arrow" style="left:95px"><svg width="14" height="16" viewBox="0 0 14 16"><path d="M11 1L3 8l8 7" fill="none" stroke="#fff" stroke-width="2.4"/></svg></div>

  <article class="card" style="left:160px">
    <div class="num">01.</div>
    <h3>HOME CLEANING</h3>
    <p>Dusting, vacuuming, mopping and polishing for every room, plus kitchens and bathrooms done properly on a schedule that suits your family life.</p>
    <span class="more">More &rarr;</span>
  </article>
  <article class="card" style="left:467px">
    <div class="num">02.</div>
    <h3>COMMERCIAL CLEANING</h3>
    <p>Tidy desks, clean floors and fresh washrooms for offices and shops, handled quietly around your opening hours by a reliable team.</p>
    <span class="more">More &rarr;</span>
  </article>
  <article class="card" style="left:762px">
    <div class="num">03.</div>
    <h3>DISCUSS YOUR REQUIREMENTS</h3>
    <p>Tell us what you need and when you need it, and we will build a simple cleaning plan and clear quote for you.</p>
    <span class="more">More &rarr;</span>
  </article>

  <div class="arrow" style="left:1060px"><svg width="14" height="16" viewBox="0 0 14 16"><path d="M3 1l8 7-8 7" fill="none" stroke="#fff" stroke-width="2.4"/></svg></div>

  <div class="case-btn">OUR CASE STUDIES</div>
</section>

<section class="works">
  <h2 class="display">OUR WORKS</h2>
  <div class="more-pill">MORE</div>
  <p>We believe our work speaks for itself. Browse our most recent projects below.</p>
</section>

<section class="grid">
  <div class="tile project" style="left:0;top:0">
    <h3>HARLOW PARK HEIGHTS</h3>
    <div class="line"></div>
    <div class="row" style="top:110px">
      <svg width="30" height="30" viewBox="0 0 30 30"><circle cx="15" cy="15" r="13" fill="none" stroke="#fff" stroke-width="1.4"/><path d="M9 17l4 4 9-10" fill="none" stroke="#fff" stroke-width="1.6"/></svg>
      LAWN CLEANING, DOMESTIC
    </div>
    <div class="row" style="top:154px">
      <svg width="30" height="30" viewBox="0 0 30 30"><circle cx="15" cy="15" r="13" fill="none" stroke="#fff" stroke-width="1.4"/><circle cx="15" cy="12" r="4" fill="none" stroke="#fff" stroke-width="1.4"/><path d="M8 23a7 7 0 0114 0" fill="none" stroke="#fff" stroke-width="1.4"/></svg>
      DANA WHITFIELD
    </div>
    <div class="testi">TESTIMONIAL</div>
  </div>
  <div class="tile" style="left:400px;top:0;background:linear-gradient(135deg,#8a5a2e,#d9a86b 50%,#6b4424)" role="img" aria-label="Photo of a cleaned hotel lounge with warm lighting"></div>
  <div class="tile" style="left:800px;top:0;background:linear-gradient(135deg,#5b4a8f,#a79ad0 50%,#3f3370)" role="img" aria-label="Photo of a cleaned restaurant dining area"></div>
  <div class="tile" style="left:0;top:289px;background:linear-gradient(135deg,#f2f2f4,#d9c9d0 50%,#e9aab8)" role="img" aria-label="Photo of a bright office stairway and reception"></div>
  <div class="tile" style="left:400px;top:289px;background:linear-gradient(135deg,#3c3566,#8f84c2 50%,#514a80)" role="img" aria-label="Photo of a covered garden walkway"></div>
  <div class="tile" style="left:800px;top:289px;background:linear-gradient(135deg,#3f7a2e,#8fc16a 50%,#2f5e24)" role="img" aria-label="Photo of a freshly tended lawn and garden"></div>
</section>

<section class="contact">
  <div class="form" role="img" aria-label="Faint photo of a happy family behind the contact form"></div>
  <h2 class="abs" style="left:34px;top:72px;font-size:20px;font-weight:500">Leave up to us and keep your family happy</h2>
  <div class="abs" style="left:34px;top:108px;width:440px;height:2px;background:var(--ink)"></div>

  <span class="lbl" style="left:34px;top:160px">Name :</span>
  <div class="field" style="left:34px;top:206px;width:230px"></div>
  <span class="lbl" style="left:306px;top:160px">Email:</span>
  <div class="field" style="left:306px;top:206px;width:230px"></div>

  <span class="lbl" style="left:34px;top:258px">Phone :</span>
  <div class="field" style="left:34px;top:316px;width:230px"></div>
  <span class="lbl" style="left:306px;top:258px">Service Required:</span>
  <div class="select">Choose our Service <svg width="8" height="6" viewBox="0 0 8 6"><path d="M0 0h8L4 6z" fill="#757575"/></svg></div>

  <span class="lbl" style="left:34px;top:358px">Message :</span>
  <div class="field" style="left:34px;top:510px;width:500px"></div>
  <div class="send">SEND</div>

  <div class="map" role="img" aria-label="Street map showing the office location"></div>

  <div class="info" style="top:0;height:200px;background:var(--blue-mid);justify-content:center">
    <svg width="34" height="44" viewBox="0 0 24 32"><path d="M12 1a10 10 0 0110 10c0 8-10 19-10 19S2 19 2 11A10 10 0 0112 1z" fill="none" stroke="#1b1b1b" stroke-width="2"/><circle cx="12" cy="11" r="3.5" fill="none" stroke="#1b1b1b" stroke-width="2"/></svg>
    <h3>LARKSPUR HOUSE</h3>
    <p>4 ORCHARD ROW, WARRINGTON,<br>WA1 2ZZ</p>
  </div>
  <div class="info" style="top:200px;height:209px;background:var(--email-grey);justify-content:center">
    <svg width="48" height="34" viewBox="0 0 48 34"><rect x="1.5" y="1.5" width="45" height="31" fill="none" stroke="#1b1b1b" stroke-width="2.4"/><path d="M2 2l22 18L46 2" fill="none" stroke="#1b1b1b" stroke-width="2.4"/></svg>
    <h3>Our Email</h3>
    <p>info@brightmeadow.co.uk</p>
  </div>
  <div class="info" style="top:409px;height:201px;background:var(--blue);justify-content:center">
    <svg width="40" height="40" viewBox="0 0 24 24"><path d="M6.6 10.8a15 15 0 006.6 6.6l2.2-2.2a1 1 0 011-.25 11.4 11.4 0 003.6.6 1 1 0 011 1V20a1 1 0 01-1 1A17 17 0 013 4a1 1 0 011-1h3.5a1 1 0 011 1 11.4 11.4 0 00.6 3.6 1 1 0 01-.25 1z" fill="none" stroke="#1b1b1b" stroke-width="1.4"/></svg>
    <h3>Call Us</h3>
    <p>100-22-480000</p>
  </div>
</section>

<footer class="footer">
  <div class="foot-brand"><span class="dot"></span><span>Bright Meadow Ltd</span></div>
  <p class="foot-text">We are a local cleaning company serving homes and businesses across the area. Our friendly team works to a high standard and treats every property with care.<br><br>Honest prices, clear communication and reliable visits are at the heart of everything we do for our customers.</p>

  <div class="foot-col" style="left:610px">
    <h4>Informations</h4>
    <div class="rule"></div>
    <ul><li>Home</li><li>What We Do</li><li>Domestic Clinic</li><li>Commercial Cleaning</li><li>Contact Us</li></ul>
  </div>
  <div class="foot-col" style="left:910px">
    <h4>Most Important Links</h4>
    <div class="rule"></div>
    <ul><li>Privacy Policy</li><li>Terms and Conditions</li><li>How to Book our Service</li><li>How we work</li><li>Cleaning Tips</li></ul>
  </div>
  <div class="to-top"><svg width="10" height="7" viewBox="0 0 10 7"><path d="M1 6l4-4 4 4" fill="none" stroke="#85acd3" stroke-width="1.6"/></svg></div>
</footer>

<div class="bottom">
  <p>All rights reserved to Bright Meadow Ltd &nbsp;|&nbsp; Designed and developed by <span style="color:var(--blue)">Northpixel</span></p>
  <div class="sq"><span></span><span></span><span></span><span></span><span></span><span></span></div>
</div>

</body>
</html>
```